One page handout design for our product specific uses

We will hire the designer to modify the selected design for multiple uses. This is the first concept. Please review the attached word document for the concept we are looking to create. The reverse side will be the same as the attached .ai file. I am including the logos for ease of working with the concept.

Need the Dunmore Vale Logo, Brisk Crest Logo. How to contact us.

```html
<!DOCTYPE html>
<html lang="en">
<head>
<meta charset="utf-8">
<title>Residential Use Handout</title>
<link href="https://fonts.googleapis.com/css2?family=Barlow:ital,wght@0,500;0,600;0,700;1,600;1,700&display=swap" rel="stylesheet">
<style>
  :root {
    --stage: #dedee0;
    --ink: #141414;
    --band: #1b1b1b;
    --yellow: #f7c716;
    --white: #ffffff;
    --photo-sky: #9fb6c4;
    --photo-wall: #d9dadb;
    --photo-dark: #2b3534;
  }
  * { box-sizing: border-box; margin: 0; padding: 0; }
  html, body {
    width: 1200px; height: 835px; overflow: hidden;
    background: var(--stage);
    font-family: "Barlow", Arial, sans-serif;
  }
  .handout {
    position: absolute; left: 298px; top: 22px;
    width: 604px; height: 790px;
    background: var(--band);
    overflow: hidden;
  }
  .header-band {
    position: absolute; left: 0; top: 0; width: 100%; height: 120px;
    background: linear-gradient(180deg, #0f0f0f, #232323);
  }
  .title-tab {
    position: absolute; left: 36px; top: 0; width: 220px; height: 92px;
    background: var(--yellow);
  }
  .title-tab h1 {
    position: absolute; left: 11px; bottom: 8px;
    font-size: 29px; font-weight: 700; color: var(--ink); letter-spacing: 0.2px;
  }
  .brand {
    position: absolute; right: 30px; top: 44px;
    display: flex; align-items: center; gap: 7px;
  }
  .brand-square { width: 14px; height: 14px; background: var(--yellow); }
  .brand-name { font-size: 25px; font-weight: 700; color: var(--white); }
  .hero-photo {
    position: absolute; left: 0; top: 119px; width: 100%; height: 537px;
    background:
      linear-gradient(90deg, rgba(40,60,62,.9) 0%, rgba(70,90,95,.6) 32%, rgba(0,0,0,0) 38%),
      linear-gradient(180deg, var(--photo-sky) 0%, var(--photo-wall) 30%, #9a9c9c 52%, var(--photo-dark) 75%, #1d2322 100%);
  }
  .usage-photo {
    position: absolute; border: 2px solid var(--yellow); border-radius: 18px 0 18px 0;
    overflow: hidden;
  }
  .usage-photo span {
    position: absolute; left: 0; bottom: 0;
    background: var(--band); color: var(--white);
    font-size: 8.5px; font-weight: 700; font-style: italic;
    padding: 3px 10px 3px 6px; border-radius: 0 8px 0 0;
  }
  .photo-bath { left: 437px; top: 323px; width: 127px; height: 131px;
    background: linear-gradient(160deg, #c9b89a, #e8e6e2 45%, #8d8a86); }
  .photo-exterior { left: 39px; top: 420px; width: 134px; height: 134px;
    border-radius: 18px 0 0 18px;
    background: linear-gradient(180deg, #b8cad6, #e4e6e6 45%, #5f6f70 75%, #3b6f86); }
  .photo-kitchen { left: 437px; top: 513px; width: 127px; height: 128px;
    background: linear-gradient(170deg, #d9d4cb, #f0eeea 45%, #8f857a); }
  .benefit-list {
    position: absolute; background: var(--yellow); list-style: none;
    padding: 6px 8px 6px 12px;
    display: flex; flex-direction: column; justify-content: center; gap: 4px;
  }
  .benefit-list li {
    display: flex; gap: 5px; align-items: flex-start;
    font-size: 8.3px; font-weight: 700; font-style: italic; line-height: 1.3; color: var(--ink);
  }
  .benefit-list svg { flex: none; width: 9px; height: 9px; margin-top: 1px; }
  .list-bath { left: 268px; top: 366px; width: 170px; height: 88px; border-radius: 14px 0 0 0; }
  .list-exterior { left: 172px; top: 470px; width: 190px; height: 77px; border-radius: 0 0 16px 0; }
  .list-kitchen { left: 169px; top: 556px; width: 269px; height: 94px; border-radius: 14px 0 0 0; }
  .footer-band {
    position: absolute; left: 0; top: 656px; width: 100%; height: 134px;
    background: linear-gradient(180deg, #111, #262626);
  }
  .cert-badge { position: absolute; }
  .cert-primary { left: 42px; top: 38px; width: 111px; height: 58px; background: var(--white); border-radius: 3px; }
  .cert-secondary { left: 168px; top: 38px; width: 52px; height: 52px; border-radius: 50%; background: #2f8fb8; border: 3px solid #d8d8d8; }
  .contact { position: absolute; right: 30px; top: 28px; text-align: right; }
  .contact-lead { font-size: 17px; font-weight: 600; color: var(--white); }
  .contact-lead em { font-style: normal; color: var(--yellow); }
  .contact-phone { font-size: 42px; font-weight: 700; color: var(--yellow); line-height: 1.05; letter-spacing: 0.5px; }
</style>
</head>
<body>
<main class="handout">
  <header class="header-band">
    <div class="title-tab"><h1>Residential Use</h1></div>
    <div class="brand"><span class="brand-square"></span><span class="brand-name">Velora</span></div>
  </header>

  <div class="hero-photo" role="img" aria-label="Modern white concrete house with glass facade, trees and a reflecting pool"></div>

  <ul class="benefit-list list-bath">
    <li><svg viewBox="0 0 10 10"><path d="M1 5.5 4 8.5 9 1.5" fill="none" stroke="#141414" stroke-width="2"/></svg>Prevents Mold and Mildew Stains From Forming on Surfaces</li>
    <li><svg viewBox="0 0 10 10"><path d="M1 5.5 4 8.5 9 1.5" fill="none" stroke="#141414" stroke-width="2"/></svg>Creates Anti-slip Surfaces</li>
    <li><svg viewBox="0 0 10 10"><path d="M1 5.5 4 8.5 9 1.5" fill="none" stroke="#141414" stroke-width="2"/></svg>Reduces Cleaning Time</li>
    <li><svg viewBox="0 0 10 10"><path d="M1 5.5 4 8.5 9 1.5" fill="none" stroke="#141414" stroke-width="2"/></svg>Eliminates Odors, VOC's And SVOC's</li>
  </ul>
  <div class="usage-photo photo-bath" role="img" aria-label="Bright interior bathroom with vanity and toilet"><span>Interior Bathrooms</span></div>

  <div class="usage-photo photo-exterior" role="img" aria-label="Exterior of a modern house beside a pool"><span>Exterior Uses</span></div>
  <ul class="benefit-list list-exterior">
    <li><svg viewBox="0 0 10 10"><path d="M1 5.5 4 8.5 9 1.5" fill="none" stroke="#141414" stroke-width="2"/></svg>Self Cleaning Surfaces with Rainwater and Light</li>
    <li><svg viewBox="0 0 10 10"><path d="M1 5.5 4 8.5 9 1.5" fill="none" stroke="#141414" stroke-width="2"/></svg>Anti-Slip Surfaces</li>
    <li><svg viewBox="0 0 10 10"><path d="M1 5.5 4 8.5 9 1.5" fill="none" stroke="#141414" stroke-width="2"/></svg>Prevent Mold and Mildew Stains from forming on Exterior Surfaces</li>
  </ul>

  <ul class="benefit-list list-kitchen">
    <li><svg viewBox="0 0 10 10"><path d="M1 5.5 4 8.5 9 1.5" fill="none" stroke="#141414" stroke-width="2"/></svg>Clean treated Surfaces with Water and a Soft Cloth</li>
    <li><svg viewBox="0 0 10 10"><path d="M1 5.5 4 8.5 9 1.5" fill="none" stroke="#141414" stroke-width="2"/></svg>Eliminate Toxic Cleaner Use</li>
    <li><svg viewBox="0 0 10 10"><path d="M1 5.5 4 8.5 9 1.5" fill="none" stroke="#141414" stroke-width="2"/></svg>Prevents Odors and Contaminates from forming on Surfaces</li>
    <li><svg viewBox="0 0 10 10"><path d="M1 5.5 4 8.5 9 1.5" fill="none" stroke="#141414" stroke-width="2"/></svg>Eliminates harmful VOC's and SVOC's from Painted Surfaces</li>
  </ul>
  <div class="usage-photo photo-kitchen" role="img" aria-label="White interior kitchen with island and pendant lights"><span>Interior Kitchens</span></div>

  <footer class="footer-band">
    <div class="cert-badge cert-primary" role="img" aria-label="Dunmore Vale certification badge"></div>
    <div class="cert-badge cert-secondary" role="img" aria-label="Brisk Crest certification badge"></div>
    <div class="contact">
      <p class="contact-lead"><em>Contact us</em> for more information</p>
      <p class="contact-phone">555 014 2290</p>
    </div>
  </footer>
</main>
</body>
</html>
```